Property inspection company needs logo/business card design

A new, home, commercial, and multi dwelling inspection company needs help with a new logo and hence business cards.

Time is extended for the rest of the week.

Font styles to use
Sans Serif

Colors
ec1f27
0255a3
ffffff

```html
<!DOCTYPE html>
<html lang="en">
<head>
<meta charset="utf-8">
<title>Whitford Property Inspections Inc — Business Card</title>
<link rel="stylesheet" href="https://fonts.googleapis.com/css2?family=Arimo:wght@400;700&display=swap">
<style>
  :root {
    --brand-red: #ec1f27;
    --brand-blue: #0255a3;
    --brand-blue-light: #1a86d6;
    --brand-white: #ffffff;
    --stage: #e9e6e1;
    --card-shadow: rgba(0, 0, 0, 0.18);
  }
  * { box-sizing: border-box; margin: 0; padding: 0; }
  html, body {
    width: 1200px;
    height: 780px;
    overflow: hidden;
  }
  body {
    background: var(--stage);
    font-family: "Arimo", Arial, sans-serif;
    position: relative;
  }
  .card {
    position: absolute;
    top: 242px;
    width: 520px;
    height: 297px;
    border-radius: 18px;
    overflow: hidden;
    box-shadow: 0 10px 28px var(--card-shadow);
  }
  .card--front { left: 50px; }
  .card--back {
    left: 630px;
    background: radial-gradient(ellipse at 45% 40%, var(--brand-blue-light) 0%, var(--brand-blue) 75%);
  }
  .card__art {
    position: absolute;
    inset: 0;
    width: 100%;
    height: 100%;
  }
  .wordmark {
    position: absolute;
    display: flex;
    align-items: center;
    gap: 9px;
    font-weight: 700;
    text-transform: uppercase;
    line-height: 1.15;
  }
  .wordmark__square {
    width: 13px;
    height: 13px;
    flex: none;
  }
  .wordmark__name { font-size: 25px; letter-spacing: 0.5px; }
  .wordmark__tag { font-size: 11px; letter-spacing: 1.8px; }
  .card--front .wordmark {
    left: 24px;
    top: 92px;
    color: var(--brand-blue);
  }
  .card--front .wordmark__square { background: var(--brand-blue); }
  .card--back .wordmark {
    left: 0;
    right: 0;
    top: 118px;
    justify-content: center;
    color: var(--brand-white);
  }
  .card--back .wordmark__square { background: var(--brand-white); }
  .address {
    position: absolute;
    right: 26px;
    top: 26px;
    color: var(--brand-white);
    font-size: 13px;
    line-height: 1.45;
    text-align: right;
  }
  .contact {
    position: absolute;
    left: 292px;
    bottom: 30px;
    color: var(--brand-white);
  }
  .contact__name { font-size: 15px; font-weight: 700; letter-spacing: 0.3px; }
  .contact__role { font-size: 13px; margin-bottom: 10px; }
  .contact__line {
    display: flex;
    align-items: center;
    gap: 7px;
    font-size: 13px;
    line-height: 1.6;
  }
  .contact__icon { width: 11px; height: 11px; flex: none; }
</style>
</head>
<body>

  <section class="card card--front" aria-label="Business card front">
    <svg class="card__art" viewBox="0 0 520 297" preserveAspectRatio="none" aria-hidden="true">
      <defs>
        <linearGradient id="frontBlue" x1="0" y1="0" x2="1" y2="1">
          <stop offset="0" stop-color="#1a86d6"/>
          <stop offset="1" stop-color="#0255a3"/>
        </linearGradient>
      </defs>
      <rect width="520" height="297" fill="url(#frontBlue)"/>
      <path d="M0 0 H372 C300 52 318 170 248 230 C225 252 222 280 222 297 H0 Z" fill="var(--brand-red)"/>
      <path d="M0 0 H348 C272 60 300 160 228 220 C205 242 202 278 200 297 H0 Z" fill="var(--brand-white)"/>
    </svg>

    <div class="wordmark">
      <span class="wordmark__square"></span>
      <span>
        <span class="wordmark__name">Whitford</span><br>
        <span class="wordmark__tag">Property Inspections Inc</span>
      </span>
    </div>

    <p class="address">4127 Larkmoor Ave.<br>Glendale, CA. 91204</p>

    <div class="contact">
      <p class="contact__name">DALE WHITFORD</p>
      <p class="contact__role">Owner</p>
      <p class="contact__line">
        <svg class="contact__icon" viewBox="0 0 12 12" aria-hidden="true">
          <path d="M2.5 1 L4.5 1 L5.3 3.6 L4 4.6 C4.7 6 6 7.3 7.4 8 L8.4 6.7 L11 7.5 L11 9.5 C11 10.3 10.3 11 9.5 11 C5 11 1 7 1 2.5 C1 1.7 1.7 1 2.5 1 Z" fill="var(--brand-white)"/>
        </svg>
        310-555-0142
      </p>
      <p class="contact__line">
        <svg class="contact__icon" viewBox="0 0 12 12" aria-hidden="true">
          <rect x="0.5" y="2" width="11" height="8" fill="none" stroke="var(--brand-white)" stroke-width="1"/>
          <path d="M0.5 2 L6 6.5 L11.5 2" fill="none" stroke="var(--brand-white)" stroke-width="1"/>
        </svg>
        dale@whitfordinspect.com
      </p>
    </div>
  </section>

  <section class="card card--back" aria-label="Business card back">
    <div class="wordmark">
      <span class="wordmark__square"></span>
      <span>
        <span class="wordmark__name">Whitford</span><br>
        <span class="wordmark__tag">Property Inspections Inc</span>
      </span>
    </div>
  </section>

</body>
</html>
```